Startup Drone Platform Company business card

We are needing a business card design for our employees. We are a startup drone platform. We are looking for a business card that has our logo on one side, with the employee/company details on the opposite side. We are looking for something that is very eye catching, modern, and bold.

Target Market(s)

This will target both drone pilots and drone businesses, along with all the industries that could utilize drone services (aerial video, aerial photos, inspections, 3d mapping, etc).

Industry/Entity Type

Business

```html
<!DOCTYPE html>
<html lang="en">
<head>
<meta charset="utf-8">
<title>Aerolet business card</title>
<link rel="stylesheet" href="https://fonts.googleapis.com/css2?family=Open+Sans:wght@400;600&family=PT+Serif&display=swap">
<style>
  :root {
    --page: #e9e7e3;
    --card-white: #ffffff;
    --card-fade: #eeeeee;
    --teal: #3fbdc4;
    --teal-deep: #2fa7ae;
    --ink: #1d1d1f;
    --ink-soft: #3a3a3c;
    --slate: #3c4f63;
    --slate-dark: #2c3a4a;
    --white: #ffffff;
  }
  * { margin: 0; padding: 0; box-sizing: border-box; }
  html, body { width: 1200px; height: 1023px; overflow: hidden; }
  body {
    background: var(--page);
    font-family: "Open Sans", sans-serif;
    position: relative;
  }
  .card {
    position: absolute;
    width: 620px;
    height: 354px;
    border-radius: 18px;
    overflow: hidden;
    box-shadow: 0 10px 28px rgba(0,0,0,0.18);
  }
  /* Front side */
  .card-front {
    left: 290px; top: 100px;
    background: linear-gradient(135deg, var(--card-fade) 0%, var(--card-white) 55%);
  }
  .identity {
    position: absolute; right: 44px; top: 34px; text-align: right;
  }
  .identity .person-name {
    color: var(--teal); font-weight: 600; font-size: 22px; letter-spacing: 0.5px;
  }
  .identity .person-title {
    color: var(--ink); font-size: 13px; margin-top: 0;
  }
  .wordmark {
    position: absolute; left: 44px; top: 178px;
    display: flex; align-items: center; gap: 12px;
  }
  .wordmark .dot {
    width: 16px; height: 16px; border-radius: 50%; background: var(--teal);
  }
  .wordmark .name {
    font-size: 26px; font-weight: 400; letter-spacing: 9px; color: var(--ink);
  }
  .contact-list {
    position: absolute; left: 44px; top: 232px; list-style: none;
    font-family: "PT Serif", serif; font-size: 14px; color: var(--ink-soft);
  }
  .contact-list li { display: flex; align-items: center; gap: 10px; height: 21px; }
  .contact-list svg { width: 12px; height: 12px; flex: none; }
  .web-band {
    position: absolute; left: 0; right: 0; bottom: 0; height: 34px;
    background: var(--teal);
    display: flex; align-items: center; justify-content: flex-end;
    padding-right: 44px;
    font-family: "PT Serif", serif; font-size: 14px; color: var(--white); letter-spacing: 0.5px;
  }
  /* Back side */
  .card-back {
    left: 290px; top: 560px;
    background: radial-gradient(circle at 60% 45%, #4b5f74 0%, var(--slate) 45%, var(--slate-dark) 100%);
    display: flex; align-items: center; justify-content: center;
  }
  .card-back .wordmark {
    position: static; gap: 16px;
  }
  .card-back .dot { width: 22px; height: 22px; }
  .card-back .name { color: var(--white); font-size: 40px; letter-spacing: 14px; }
</style>
</head>
<body>
  <section class="card card-front" aria-label="Card front">
    <div class="identity">
      <p class="person-name">Employer Name</p>
      <p class="person-title">Title</p>
    </div>

    <div class="wordmark">
      <span class="dot"></span>
      <span class="name">AEROLET</span>
    </div>

    <ul class="contact-list">
      <li>
        <svg viewBox="0 0 12 12"><path d="M3 1 L5 3.5 L4 5 Q5 7 7 8 L8.5 7 L11 9 L10 11 Q4 11 1 2 Z" fill="#3fbdc4"/></svg>
        88 100 20030
      </li>
      <li>
        <svg viewBox="0 0 12 12"><rect x="0.5" y="2" width="11" height="8" fill="#3fbdc4"/><path d="M0.5 2 L6 6.5 L11.5 2" stroke="#fff" stroke-width="1.2" fill="none"/></svg>
        name@aerolethire.com
      </li>
      <li>
        <svg viewBox="0 0 12 12"><rect x="0.5" y="0.5" width="11" height="11" fill="#3fbdc4"/></svg>
        social.aerolethire.com/idname
      </li>
    </ul>

    <div class="web-band">www.aerolethire.com</div>
  </section>

  <section class="card card-back" aria-label="Card back">
    <div class="wordmark">
      <span class="dot"></span>
      <span class="name">AEROLET</span>
    </div>
  </section>
</body>
</html>
```